Technical Refinement & Corporate Adaptation of AI Graphics

We have a follow-up project for you that involves technically refining existing, AI-generated graphics and recreating them professionally in Microsoft PowerPoint. - as you did already. The content and core structure should remain unchanged, but the visual style needs to be aligned with the corporate design of the Kraftwerkhaus Morlen (colors, typography, and visual language). The primary focus is to ensure all elements are fully editable, perfectly aligned, and deliver a clean, scientific-technical look.

```html
<!DOCTYPE html>
<html lang="en">
<head>
<meta charset="utf-8">
<title>District Heating, Waste Heat &amp; Thermal Storage</title>
<link href="https://fonts.googleapis.com/css2?family=Fira+Sans+Condensed:wght@400;500;600;700&family=Fira+Sans:wght@400;500&display=swap" rel="stylesheet">
<style>
  :root{
    --green-dark:#2f3d1e;
    --green:#6b8a3a;
    --green-mid:#7f9b52;
    --green-soft:#b9c8a3;
    --tint:#eef2ea;
    --panel:#fbfcfa;
    --text:#333a2c;
    --line:#c9d4bb;
    --bg:#ffffff;
  }
  *{box-sizing:border-box;margin:0;padding:0}
  html,body{width:1200px;height:675px;overflow:hidden;background:var(--bg)}
  .canvas{position:relative;width:1200px;height:675px;overflow:hidden;background:var(--bg);
    font-family:"Fira Sans Condensed",sans-serif;color:var(--text)}
  .abs{position:absolute}

  /* header */
  .section-number{left:106px;top:17px;width:77px;height:77px;border-radius:50%;background:var(--green);
    color:#fff;font-weight:600;font-size:50px;display:flex;align-items:center;justify-content:center}
  .title{left:204px;top:17px;font-weight:700;font-size:38px;letter-spacing:-.6px;color:var(--green-dark);white-space:nowrap}
  .subtitle{left:205px;top:61px;font-family:"Fira Sans",sans-serif;font-size:23px;color:#4a4a44;white-space:nowrap}
  .deco-lines{left:0;top:0}

  /* panels */
  .panel{border:1.3px solid var(--green-soft);border-radius:12px;background:var(--panel)}
  .panel-label{left:0;right:0;display:flex;justify-content:center;align-items:center;gap:12px;
    font-family:"Fira Sans",sans-serif;font-weight:500;font-size:12.5px;letter-spacing:3.6px;color:var(--green-dark)}
  .panel-label::before,.panel-label::after{content:"";width:80px;height:1px;background:var(--green-mid)}
  .value-chain{left:25px;top:113px;width:1151px;height:265px}
  .methods{left:25px;top:388px;width:1151px;height:100px}
  .benefits{left:79px;top:500px;width:1094px;height:121px}

  /* value chain cards */
  .stage{top:139px;width:178px;height:228px;border:1px solid #d9e0d0;border-radius:9px;background:#fff}
  .stage-badge{left:15px;top:11px;width:30px;height:30px;border-radius:50%;background:var(--green);color:#fff;
    font-weight:600;font-size:18px;display:flex;align-items:center;justify-content:center;box-shadow:0 0 0 3px var(--tint)}
  .stage-title{left:56px;top:11px;height:30px;display:flex;align-items:center;font-weight:500;font-size:14.5px;
    line-height:16px;color:var(--green-dark)}
  .stage-icon{left:34px;top:49px;width:110px;height:110px;border-radius:50%;background:var(--tint);
    display:flex;align-items:center;justify-content:center}
  .stage-rule{left:25px;top:156px;width:130px;height:1px;background:var(--line)}
  .stage-text{left:4px;right:4px;top:172px;text-align:center;font-size:13.5px;line-height:18px;color:var(--text)}
  .flow-arrow{width:10px;height:28px}

  /* methods */
  .method-icon{top:418px;width:56px;height:56px;border-radius:50%;background:var(--tint);
    display:flex;align-items:center;justify-content:center}
  .method-text{top:428px;font-size:13.5px;line-height:18px;color:var(--text)}
  .divider{width:1px;background:var(--line)}

  /* benefits */
  .benefit-icon{top:530px;width:48px;height:72px;display:flex;align-items:center;justify-content:center}
  .benefit-text{font-size:13.5px;line-height:18px;color:var(--text)}

  .city-photo{left:0;top:481px;width:158px;height:194px;
    clip-path:polygon(0 0,100% 100%,0 100%);
    background:linear-gradient(160deg,#a9bd9a 0%,#6f8f5a 45%,#3f5e2e 100%)}
  .footer-line{left:184px;top:645px;width:980px}
  .footer-text{left:0;right:0;top:639px;text-align:center;font-family:"Fira Sans",sans-serif;font-size:9.5px;
    letter-spacing:1.6px;color:var(--green-dark)}
  .footer-text span{background:var(--bg);padding:0 14px}
</style>
</head>
<body>
<div class="canvas">

  <svg class="abs deco-lines" width="1200" height="120" aria-hidden="true">
    <path d="M34 104 V62 Q34 59 37 59 H88" fill="none" stroke="var(--green-mid)" stroke-width="1.2"/>
    <circle cx="90" cy="59" r="4.5" fill="var(--green-mid)"/>
    <line x1="990" y1="77" x2="1162" y2="77" stroke="var(--green-mid)" stroke-width="1.2"/>
    <circle cx="1164" cy="77" r="4.5" fill="var(--green-mid)"/>
  </svg>

  <div class="abs section-number">4</div>
  <h1 class="abs title">District Heating, Waste Heat &amp; Thermal Storage</h1>
  <p class="abs subtitle">Efficient and sustainable heat solutions for industry and communities</p>

  <!-- value chain -->
  <section class="abs panel value-chain"></section>
  <div class="abs panel-label" style="top:121px">VALUE CHAIN</div>

  <div class="abs stage" style="left:34px">
    <div class="abs stage-badge">1</div><div class="abs stage-title">Heat Sources</div>
    <div class="abs stage-icon">
      <svg width="64" height="64" viewBox="0 0 64 64" fill="none" stroke="var(--green-dark)" stroke-width="2.2" stroke-linejoin="round">
        <path d="M6 58 V24 H14 V58 M14 40 L24 32 V40 L34 32 V40 L44 32 V58 H6"/>
        <path d="M8 20 Q12 14 16 16 Q20 8 26 10"/><rect x="12" y="46" width="5" height="4"/><rect x="21" y="46" width="5" height="4"/><rect x="30" y="46" width="5" height="4"/>
        <path d="M46 40 H58 V58 H44 M49 48 H55"/>
        <path d="M46 16 Q42 20 46 24 Q50 28 46 32 M52 14 Q48 18 52 22 Q56 26 52 30 M58 16 Q54 20 58 24 Q62 28 58 32"/>
      </svg>
    </div>
    <div class="abs stage-rule"></div>
    <p class="abs stage-text">Industrial waste heat,<br>geothermal, solar thermal,<br>CHP, heat pumps, P2H</p>
  </div>

  <div class="abs stage" style="left:223px">
    <div class="abs stage-badge">2</div><div class="abs stage-title">Conversion &amp;<br>Upgrading</div>
    <div class="abs stage-icon">
      <svg width="64" height="64" viewBox="0 0 64 64" fill="none" stroke="var(--green-dark)" stroke-width="2.2" stroke-linejoin="round">
        <rect x="8" y="14" width="12" height="36" rx="4"/><rect x="44" y="14" width="12" height="36" rx="4"/>
        <path d="M20 20 H44 M20 44 H44"/><rect x="26" y="24" width="12" height="16"/><path d="M30 27 V37 M34 27 V37"/>
        <path d="M11 10 H17 M47 10 H53 M11 54 H17 M47 54 H53 M5 24 H8 M5 40 H8 M56 24 H59 M56 40 H59"/>
      </svg>
    </div>
    <div class="abs stage-rule"></div>
    <p class="abs stage-text">Heat pumps, boiler,<br>electric heaters,<br>steam systems</p>
  </div>

  <div class="abs stage" style="left:416px">
    <div class="abs stage-badge">3</div><div class="abs stage-title">Thermal Storage</div>
    <div class="abs stage-icon">
      <svg width="64" height="64" viewBox="0 0 64 64" fill="none" stroke="var(--green-dark)" stroke-width="2.2">
        <ellipse cx="26" cy="16" rx="20" ry="6"/><path d="M6 16 V50 Q26 60 46 50 V16 M6 46 Q26 56 46 46"/>
        <path d="M23 8 H29" /><path d="M26 26 Q21 33 21 36 A5 5 0 0 0 31 36 Q31 33 26 26Z" fill="var(--green-dark)"/>
        <rect x="51" y="24" width="6" height="20" rx="3"/><circle cx="54" cy="48" r="5"/>
      </svg>
    </div>
    <div class="abs stage-rule"></div>
    <p class="abs stage-text">Short-term (hot water,<br>sensible, latent,<br>thermochemical)</p>
  </div>

  <div class="abs stage" style="left:607px">
    <div class="abs stage-badge">4</div><div class="abs stage-title">Heat Networks</div>
    <div class="abs stage-icon">
      <svg width="72" height="64" viewBox="0 0 72 64" fill="none" stroke="var(--green-dark)" stroke-width="2.2" stroke-linejoin="round">
        <path d="M4 44 V38 H22 V26 H30 V38 H48 V44 M4 50 H70 M4 56 H70 M12 38 V50 M36 44 V50"/>
        <rect x="20" y="22" width="12" height="4"/><rect x="40" y="44" width="8" height="16" rx="2"/>
        <rect x="54" y="4" width="12" height="34"/><path d="M57 10 H63 M57 16 H63 M57 22 H63 M57 28 H63 M60 38 V50"/>
      </svg>
    </div>
    <div class="abs stage-rule"></div>
    <p class="abs stage-text">District heating,<br>low-temperature<br>networks</p>
  </div>

  <div class="abs stage" style="left:798px">
    <div class="abs stage-badge">5</div><div class="abs stage-title">End Uses</div>
    <div class="abs stage-icon">
      <svg width="72" height="64" viewBox="0 0 72 64" fill="none" stroke="var(--green-dark)" stroke-width="2.2" stroke-linejoin="round">
        <path d="M2 60 H70"/><rect x="6" y="24" width="14" height="36"/><rect x="24" y="10" width="16" height="50"/><path d="M28 10 V4 H36 V10"/>
        <path d="M40 60 V40 L54 28 L68 40 V60 M49 60 V48 H59 V60"/>
        <path d="M10 30 H16 M10 38 H16 M10 46 H16 M28 18 H36 M28 26 H36 M28 34 H36 M28 42 H36 M28 50 H36"/>
      </svg>
    </div>
    <div class="abs stage-rule"></div>
    <p class="abs stage-text">Industry, buildings,<br>services, public<br>facilities</p>
  </div>

  <div class="abs stage" style="left:989px">
    <div class="abs stage-badge">6</div><div class="abs stage-title">Optimization &amp;<br>Operation</div>
    <div class="abs stage-icon">
      <svg width="72" height="64" viewBox="0 0 72 64" fill="none" stroke="var(--green-dark)" stroke-width="2.4" stroke-linejoin="round">
        <rect x="4" y="6" width="64" height="42" rx="3"/><path d="M28 48 L26 58 H46 L44 48 M20 58 H52"/>
        <circle cx="24" cy="26" r="6"/><path d="M24 15 V19 M24 33 V37 M13 26 H17 M31 26 H35 M16 18 L19 21 M29 31 L32 34 M32 18 L29 21 M19 31 L16 34"/>
        <path d="M42 36 V28 M49 36 V22 M56 36 V16" stroke-width="4"/>
      </svg>
    </div>
    <div class="abs stage-rule"></div>
    <p class="abs stage-text">Load matching,<br>control strategies,<br>flexibility</p>
  </div>

  <svg class="abs" width="1200" height="300" style="left:0;top:0" aria-hidden="true">
    <g fill="var(--green-mid)">
      <polygon points="215,229 229,243 215,257"/><polygon points="407,229 421,243 407,257"/>
      <polygon points="598,229 612,243 598,257"/><polygon points="789,229 803,243 789,257"/>
      <polygon points="980,229 994,243 980,257"/>
    </g>
  </svg>

  <!-- methods & tools -->
  <section class="abs panel methods"></section>
  <div class="abs panel-label" style="top:396px">METHODS &amp; TOOLS</div>

  <div class="abs method-icon" style="left:55px">
    <svg width="40" height="40" viewBox="0 0 40 40" fill="none" stroke="var(--green-dark)" stroke-width="2">
      <path d="M8 12 A15 15 0 0 1 32 10 M32 28 A15 15 0 0 1 8 30"/><path d="M30 5 L32 10 L27 11 M10 35 L8 30 L13 29"/>
      <path d="M20 12 Q28 20 24 27 Q20 30 16 27 Q12 20 20 12Z M20 18 V30"/>
    </svg>
  </div>
  <p class="abs method-text" style="left:126px">Energy &amp; exergy<br>analysis</p>
  <div class="abs divider" style="left:237px;top:422px;height:46px"></div>

  <div class="abs method-icon" style="left:258px">
    <svg width="40" height="40" viewBox="0 0 40 40" fill="none" stroke="var(--green-dark)" stroke-width="2">
      <circle cx="20" cy="20" r="5"/><circle cx="20" cy="5" r="3.5"/><circle cx="5" cy="20" r="3.5"/><circle cx="35" cy="20" r="3.5"/><circle cx="20" cy="35" r="3.5"/>
      <path d="M20 9 V15 M9 20 H15 M25 20 H31 M20 25 V31"/>
    </svg>
  </div>
  <p class="abs method-text" style="left:327px">Network<br>modeling</p>
  <div class="abs divider" style="left:410px;top:422px;height:46px"></div>

  <div class="abs method-icon" style="left:429px">
    <svg width="40" height="40" viewBox="0 0 40 40" fill="none" stroke="var(--green-dark)" stroke-width="2">
      <rect x="8" y="7" width="24" height="30" rx="3"/><path d="M15 4 H25 V9 H15Z"/>
      <path d="M25 17 A7 7 0 1 0 25 29 M13 21 H22 M13 25 H22"/>
    </svg>
  </div>
  <p class="abs method-text" style="left:498px">Techno-economic<br>assessment (TEA)</p>
  <div class="abs divider" style="left:615px;top:422px;height:46px"></div>

  <div class="abs method-icon" style="left:633px">
    <svg width="40" height="40" viewBox="0 0 40 40" fill="var(--green)">
      <path d="M20 4 Q28 12 20 22 Q12 12 20 4Z"/><path d="M18 24 Q8 14 3 20 Q6 30 18 24Z"/><path d="M22 24 Q32 14 37 20 Q34 30 22 24Z"/><path d="M19 22 H21 V34 H19Z"/>
    </svg>
  </div>
  <p class="abs method-text" style="left:703px;top:437px">eLCA</p>
  <div class="abs divider" style="left:764px;top:422px;height:46px"></div>

  <div class="abs method-icon" style="left:783px">
    <svg width="40" height="40" viewBox="0 0 40 40" fill="none" stroke="var(--green-dark)" stroke-width="3" stroke-dasharray="3 2.5">
      <circle cx="25" cy="13" r="7"/><circle cx="13" cy="27" r="7"/><circle cx="29" cy="31" r="5"/>
    </svg>
  </div>
  <p class="abs method-text" style="left:852px">Optimization &amp;<br>simulation</p>
  <div class="abs divider" style="left:961px;top:422px;height:46px"></div>

  <div class="abs method-icon" style="left:983px">
    <svg width="40" height="40" viewBox="0 0 40 40" fill="none" stroke="var(--green-dark)" stroke-width="2">
      <circle cx="20" cy="20" r="16" stroke-dasharray="2 3"/><path d="M8 27 L16 19 L22 24 L31 13 M26 13 H31 V18"/>
    </svg>
  </div>
  <p class="abs method-text" style="left:1053px">Sensitivity &amp;<br>scenario analysis</p>

  <!-- benefits & results -->
  <section class="abs panel benefits"></section>
  <div class="abs panel-label" style="top:508px">BENEFITS &amp; RESULTS</div>

  <div class="abs benefit-icon" style="left:112px;width:56px">
    <svg width="56" height="64" viewBox="0 0 56 64" fill="none" stroke="var(--green)" stroke-width="3">
      <path d="M4 30 L18 18 L28 26 L50 6 M40 6 H52 V18"/>
      <path d="M6 62 V44 M17 62 V38 M28 62 V32 M39 62 V26 M50 62 V22" stroke-width="7"/>
    </svg>
  </div>
  <p class="abs benefit-text" style="left:180px;top:544px">Higher energy<br>efficiency</p>
  <div class="abs divider" style="left:277px;top:534px;height:62px"></div>

  <div class="abs benefit-icon" style="left:305px;width:52px">
    <svg width="52" height="64" viewBox="0 0 52 64" fill="none" stroke="var(--green-dark)" stroke-width="2.4" stroke-linecap="round">
      <path d="M12 50 Q2 20 46 6 Q50 44 12 50Z"/><path d="M6 62 L36 18"/>
    </svg>
  </div>
  <p class="abs benefit-text" style="left:372px;top:544px">Lower emissions<br>and costs</p>
  <div class="abs divider" style="left:492px;top:534px;height:62px"></div>

  <div class="abs benefit-icon" style="left:523px;width:54px">
    <svg width="54" height="66" viewBox="0 0 54 66" fill="none" stroke="var(--green-dark)" stroke-width="2.2" stroke-linejoin="round">
      <path d="M2 64 V50 L14 44 V50 L26 44 V50 L38 44 V50 L52 44 V64 Z M8 50 V30 H14 V44"/>
      <path d="M10 56 H14 M20 56 H24 M30 56 H34 M40 56 H44"/>
      <path d="M22 24 Q18 18 22 12 Q26 6 22 2 M32 24 Q28 18 32 12 Q36 6 32 2 M42 24 Q38 18 42 12 Q46 6 42 2"/>
    </svg>
  </div>
  <p class="abs benefit-text" style="left:609px;top:538px">Better use of<br>waste heat<br>resources</p>
  <div class="abs divider" style="left:718px;top:534px;height:62px"></div>

  <div class="abs benefit-icon" style="left:750px">
    <svg width="48" height="62" viewBox="0 0 48 62" fill="none" stroke="var(--green-dark)" stroke-width="2.6" stroke-linejoin="round">
      <path d="M24 2 L44 10 V28 Q44 48 24 60 Q4 48 4 28 V10 Z"/><path d="M14 30 L22 38 L35 22"/>
    </svg>
  </div>
  <p class="abs benefit-text" style="left:820px;top:538px">Resilient and<br>flexible heat<br>supply</p>
  <div class="abs divider" style="left:925px;top:534px;height:62px"></div>

  <div class="abs benefit-icon" style="left:950px;width:70px">
    <svg width="70" height="64" viewBox="0 0 70 64" fill="none" stroke="var(--green-dark)" stroke-width="2.4" stroke-linejoin="round">
      <path d="M12 20 V12 H22 V8 H30 V2 H40 V8 H48 V14 H58 V20"/>
      <circle cx="14" cy="34" r="6"/><circle cx="35" cy="30" r="7"/><circle cx="56" cy="34" r="6"/>
      <path d="M2 60 V50 Q2 44 14 44 Q26 44 26 50 V60 M22 60 V46 Q22 40 35 40 Q48 40 48 46 V60 M44 60 V50 Q44 44 56 44 Q68 44 68 50 V60 M2 60 H68"/>
    </svg>
  </div>
  <p class="abs benefit-text" style="left:1034px;top:538px">Support for<br>industrial and urban<br>transformation</p>

  <div class="abs city-photo" role="img" aria-label="Photo of green urban buildings surrounded by trees"></div>

  <svg class="abs footer-line" width="980" height="10" style="top:640px" aria-hidden="true">
    <circle cx="4" cy="5" r="4" fill="var(--green-mid)"/><line x1="4" y1="5" x2="976" y2="5" stroke="var(--green-mid)" stroke-width="1.2"/><circle cx="976" cy="5" r="4" fill="var(--green-mid)"/>
  </svg>
  <p class="abs footer-text"><span>TOWARDS A CLEANER, MORE RESILIENT AND ENERGY EFFICIENT SOCIETY</span></p>

</div>
</body>
</html>
```